Contemporary Business card for Event Manager

Needed for my startup events company in Melbourne. Events I manage will be based within the fashion industry, sporting events, product launches etc. Not weddings or small dinner parties. Therfore I am after something professional and aimed at high end corporate market; but with the added emphasis on not being too conservative or boring. I am happy with a pop of colour e.g. yellow or copper foil.

Target Market(s)

fashion industry, design industry, high end sporting events e.g. Polo, Grand Prix, corporate clients,

Industry/Entity Type

Fashion

Contact Information for Business Card

side 1
Lena Varsby (can be upper or lower case, have a feature full stop between first and surname, or at the end of the nameetc) I am open to ideas. I would also be fine with my initials or name as a logo on the front (if this is the case my full name would need to go on the second side of the card.
2nd side:
Mobile: +61 491 570 156
email: lena.varsby@mailtrove.com.au

on one side of the card:
event management | brand activation | Advisory Services

Font styles to use
Serif
Sans Serif

Requirements
Must have
• side 2 must have
• mobile number
• email address
• event management | brand activation | Advisory Services
• ** my full name (Lena Varsby) must be on the card somewhere)
Nice to have
• 1st side
• I see the card stock being either a dark grey, light grey, natural white or black (all matt colours on unprocessed card). I see the writing being copper foil, or foil white or foil black.
• To give you a feel for me, think: contemporary, minimalist, I love line drawings, concrete, white with grey vein marble, copper, white, grey, black...yes I do like colour....yellow (but pops of colour) ;) I would like the card to look designer but 'on trend' as I deal with a lot of design and fashion clients....styles - think the sophistication and simplicity of Morvane or urban contemporary.
• some examples of what I like. Although please don't leet this limit you...I really am happy to have something a little more urban or design focused like a line drawing of an object, person too or a photo image too.
• https://www.moodfolia.com/pin/100000000000000001/
• https://www.moodfolia.com/pin/100000000000000002/
• https://www.moodfolia.com/pin/100000000000000003/
• https://www.moodfolia.com/pin/10000000000000004/
• https://www.moodfolia.com/pin/10000000000000005/
• https://www.moodfolia.com/pin/10000000000000006/
• https://www.moodfolia.com/pin/100000000000000007/
• https://www.moodfolia.com/pin/100000000000000008/
• https://www.moodfolia.com/pin/100000000000000009/
Should not have
• should not look commercial or have cartoonish looking logos. However happy with a simple line drawing or logo with initials etc.

```html
<!DOCTYPE html>
<html lang="en">
<head>
<meta charset="utf-8">
<title>Lena Varsby – Business Card</title>
<link rel="stylesheet" href="https://fonts.googleapis.com/css2?family=Urbanist:wght@400;500;700&display=swap">
<style>
  :root {
    --backdrop: #e6e4e1;
    --card-front: #ffffff;
    --card-back: #1f1f1f;
    --ink: #111111;
    --emboss: #2b2b2b;
    --card-shadow: rgba(0, 0, 0, 0.18);
  }
  * { margin: 0; padding: 0; box-sizing: border-box; }
  html, body {
    width: 1200px;
    height: 1000px;
    overflow: hidden;
    background: var(--backdrop);
    font-family: "Urbanist", "Century Gothic", sans-serif;
  }
  .canvas { position: relative; width: 1200px; height: 1000px; }

  .card {
    position: absolute;
    left: 265px;
    width: 666px;
    height: 397px;
    box-shadow: 0 4px 14px var(--card-shadow);
  }
  .card--front { top: 73px; background: var(--card-front); color: var(--ink); }
  .card--back  { top: 532px; background: var(--card-back); }

  .front-mark {
    position: absolute;
    top: 70px;
    right: 40px;
    font-size: 74px;
    font-weight: 400;
    line-height: 1;
    letter-spacing: -1px;
    color: var(--ink);
  }

  .contact {
    position: absolute;
    left: 38px;
    top: 228px;
  }
  .contact__name {
    font-size: 19px;
    font-weight: 700;
    margin-bottom: 22px;
  }
  .contact__line {
    display: flex;
    align-items: center;
    gap: 6px;
    font-size: 16.5px;
    line-height: 23px;
  }
  .contact__line svg { width: 13px; height: 13px; flex: none; }
  .contact__services {
    font-size: 17px;
    margin-top: 17px;
    word-spacing: 1px;
  }

  .back-mark {
    position: absolute;
    left: 0;
    right: 0;
    top: 110px;
    text-align: center;
    font-size: 96px;
    font-weight: 400;
    line-height: 1;
    color: var(--emboss);
  }
  .back-name {
    position: absolute;
    left: 0;
    right: 0;
    top: 278px;
    text-align: center;
    font-size: 29px;
    font-weight: 700;
    color: var(--emboss);
  }
</style>
</head>
<body>
<main class="canvas">
  <section class="card card--front">
    <div class="front-mark">Lena Varsby</div>
    <div class="contact">
      <p class="contact__name">Lena Varsby</p>
      <p class="contact__line">
        <svg viewBox="0 0 16 16" aria-hidden="true"><path d="M3 1.5l3 .5 1 3.5-2 1.3a8 8 0 0 0 4.2 4.2l1.3-2 3.5 1 .5 3c-.2.8-.9 1.5-1.8 1.5C6.5 14.5 1.5 9.5 1.5 3.3 1.5 2.4 2.2 1.7 3 1.5z" fill="#111"/></svg>
        +61 491 570 156
      </p>
      <p class="contact__line">
        <svg viewBox="0 0 16 16" aria-hidden="true"><rect x="1" y="3" width="14" height="10" fill="#111"/><path d="M1.5 3.5L8 9l6.5-5.5" stroke="#fff" stroke-width="1.4" fill="none"/></svg>
        lena.varsby@mailtrove.com.au
      </p>
      <p class="contact__services">Event Management &nbsp;|&nbsp; Brand Activation &nbsp;|&nbsp; Advisory Services</p>
    </div>
  </section>

  <section class="card card--back">
    <div class="back-mark">Lena Varsby</div>
    <p class="back-name">Lena Varsby</p>
  </section>
</main>
</body>
</html>
```